K & R Acreage Works. Business card design

We need a business card designed for a new business. We have a bulldozer and tractor service. We clear land and make wildlife food plots. We provide disking, bush hogging, and site prep services.
I have attached an image of a business card that I like and would like my business cards to look similar.

Target Market(s)

anyone needing bulldozer and/or tractor services

Industry/Entity Type

Business

Contact Information for Business Card

K & R Acreage Works, Operated by 7-M-Ranch
Doug Pelham
601-473-5826
dpr4178@mailvexo.com

Font styles to use
Sans Serif

Colors

Designer to choose colors to be used in the design.

Requirements
Must have
• image of tractor and bulldozer
• Land Clearing
• Wildlife food plots
• Bush Hogging
• Disking
• Site prep
Nice to have
• i have included a image of a business card that i like. I would like mine to be similar.

```html
<!DOCTYPE html>
<html lang="en">
<head>
<meta charset="utf-8">
<title>K &amp; R Acreage Works — Business Card</title>
<link rel="stylesheet" href="https://fonts.googleapis.com/css2?family=Oswald:wght@500&family=Montserrat:wght@500&family=Open+Sans:wght@400&family=Roboto+Condensed:wght@400&display=swap">
<style>
  :root{
    --page:#e9e9e7;
    --card-dark:#353230;
    --band:rgba(255,255,255,0.82);
    --green:#2f9a3e;
    --gold:#d9a21f;
    --brown-gold:#a57a1c;
    --light-green:#8cc152;
    --white:#ffffff;
  }
  *{margin:0;padding:0;box-sizing:border-box}
  html,body{width:1200px;height:900px;overflow:hidden;background:var(--page)}
  .card{
    position:absolute;left:75px;top:150px;width:1050px;height:600px;
    border-radius:34px;overflow:hidden;background:var(--card-dark);
  }
  .hero-photo{
    position:absolute;left:0;top:0;width:100%;height:356px;
    background:
      linear-gradient(180deg,rgba(170,200,225,0.9) 0%,rgba(170,200,225,0) 14%),
      linear-gradient(90deg,#9b2a22 0%,#7a3a2a 8%,#2f7a2c 18%,#3a8a30 33%,#5d7a3a 45%,#8a7650 56%,#b39a3a 66%,#c7b032 76%,#3a3a32 88%,#5a6a3a 100%);
  }
  .hero-rule{position:absolute;left:0;top:354px;width:100%;height:5px;background:var(--white)}
  .title-band{
    position:absolute;left:0;top:39px;width:100%;height:89px;background:var(--band);
    display:flex;align-items:baseline;gap:10px;padding:16px 0 0 44px;white-space:nowrap;
  }
  .title-initials,.title-name{
    font-family:'Oswald',sans-serif;font-weight:500;font-size:60px;line-height:1;
    letter-spacing:-0.5px;text-transform:uppercase;
  }
  .title-initials{color:var(--green)}
  .title-name{color:var(--gold)}
  .title-operator{font-family:'Montserrat',sans-serif;font-weight:500;font-size:30px;color:var(--brown-gold);text-transform:uppercase}
  .brand-mark{
    position:absolute;left:0;width:100%;top:378px;
    display:flex;justify-content:center;align-items:center;gap:12px;
    font-family:'Open Sans',sans-serif;font-weight:400;font-size:26px;color:var(--white);
  }
  .brand-dot{width:18px;height:18px;border-radius:50%;background:var(--light-green)}
  .person{position:absolute;left:38px;top:372px}
  .person-name{font-family:'Roboto Condensed',sans-serif;font-size:37px;color:var(--gold);line-height:1.05}
  .person-role{font-family:'Open Sans',sans-serif;font-size:29px;color:var(--light-green);line-height:1.2}
  .contact{position:absolute;left:38px;display:flex;align-items:center;gap:28px;
    font-family:'Roboto Condensed',sans-serif;font-size:23px;color:var(--white)}
  .contact-phone{top:478px}
  .contact-email{top:531px}
  .contact svg{width:28px;height:28px;fill:var(--white)}
  .services{position:absolute;right:41px;top:372px;text-align:right;font-family:'Open Sans',sans-serif}
  .services-heading{font-size:29px;color:var(--light-green);margin-bottom:8px}
  .services-list{list-style:none;font-size:22px;color:var(--white);line-height:29px}
</style>
</head>
<body>
  <div class="card">
    <div class="hero-photo" role="img" aria-label="Photo of a green tractor with a red trailer beside a yellow bulldozer clearing land"></div>
    <div class="title-band">
      <span class="title-initials">K &amp; R</span>
      <span class="title-name">Acreage Works</span>
      <span class="title-operator">Operated by 7-M-Ranch</span>
    </div>
    <div class="hero-rule"></div>

    <div class="brand-mark">
      <span class="brand-dot" aria-hidden="true"></span>
      <span class="brand-name">K &amp; R</span>
    </div>

    <div class="person">
      <div class="person-name">Doug Pelham</div>
      <div class="person-role">Owner</div>
    </div>

    <div class="contact contact-phone">
      <svg viewBox="0 0 24 24" aria-hidden="true"><path d="M6.6 10.8a15.1 15.1 0 0 0 6.6 6.6l2.2-2.2a1 1 0 0 1 1-.25 11.4 11.4 0 0 0 3.6.57 1 1 0 0 1 1 1V20a1 1 0 0 1-1 1A17 17 0 0 1 3 4a1 1 0 0 1 1-1h3.5a1 1 0 0 1 1 1c0 1.250.2 2.45.57 3.6a1 1 0 0 1-.25 1z"/></svg>
      <span>601-473-5826</span>
    </div>
    <div class="contact contact-email">
      <svg viewBox="0 0 24 24" aria-hidden="true"><path d="M12 2 2 8v13h20V8zm0 2.3L19.5 8 12 12.6 4.5 8zM4 19v-8.7l8 4.9 8-4.9V19z"/></svg>
      <span>dpr4178@mailvexo.com</span>
    </div>

    <div class="services">
      <div class="services-heading">What we provide:</div>
      <ul class="services-list">
        <li>Land Clearing</li>
        <li>Wildlife food plots</li>
        <li>Bush Hogging</li>
        <li>Disking</li>
        <li>Site prep</li>
      </ul>
    </div>
  </div>
</body>
</html>
```